Styling of small website for mid-sized Engineering and Manufacturing company

We need the styling for a professional website for a company wich delivers: engineering, manufacturing, assembling, servicing and prototyping. (typically, they produce complex devices in limited series (1-100 pieces. The client comes with an idea and they translate it into design and device).
We have already made a wire-frame, but need a style (colors, fonts, H1, H2, paragraphs, margins, padding etc).
The style must :
- express profession attitude (world of engineering)
- have a fresh, modern look
- be sober (enough (white) space between the elements
The style must also be able to be used in a RWD. At this moment the logo (just letters) uses a green color (#4C6E33), but it isn't an obligation to use the exact same color (even not the 'green' color itself if you think another color is better for the site).
engineering and production
It Company
Coded - Design and coding required
5+ page

```html
<!DOCTYPE html>
<html lang="en">
<head>
<meta charset="utf-8">
<title>Vantora — Technological Solutions</title>
<link href="https://fonts.googleapis.com/css2?family=Roboto:wght@300;400;500;700&display=swap" rel="stylesheet">
<style>
:root{
  --orange:#e35c10;
  --orange-dark:#c94f0b;
  --ink:#222;
  --text:#444;
  --muted:#555;
  --line:#dcdcdc;
  --footer:#e0e0e0;
  --white:#fff;
}
*{margin:0;padding:0;box-sizing:border-box}
html,body{width:1040px;height:1200px;overflow:hidden;background:var(--white)}
body{font-family:'Roboto',sans-serif;color:var(--text);position:relative}
.abs{position:absolute}

/* header */
.header{left:0;top:0;width:1040px;height:66px;background:var(--white)}
.brand{left:66px;top:27px;font-size:26px;font-weight:700;color:var(--orange);letter-spacing:-0.5px;line-height:1;display:flex;align-items:center;gap:6px}
.brand-dot{width:10px;height:10px;background:var(--orange)}
.nav{right:64px;top:26px;display:flex;align-items:center;height:31px}
.nav a{font-size:11.5px;color:var(--ink);text-decoration:none;padding:0 20px;line-height:31px;letter-spacing:.2px}
.nav a:last-child{padding-right:0}
.nav a.active{background:var(--orange);color:var(--white);padding:0 18px;margin-right:2px}

/* hero */
.hero{left:0;top:66px;width:1040px;height:420px;background:linear-gradient(90deg,#5f93d4 0%,#4d82c6 35%,#2f5e9f 60%,#23498a 100%)}
.hero-title{left:65px;top:140px;font-size:37px;font-weight:500;line-height:37px;color:var(--white);text-shadow:0 1px 3px rgba(0,0,0,.35)}
.hero-copy{left:65px;top:226px;width:440px;font-size:14.4px;line-height:21.6px;color:var(--white);font-weight:400}
.btn{left:65px;top:352px;width:107px;height:36px;background:var(--orange);color:var(--white);font-size:12.8px;line-height:36px;text-align:center;letter-spacing:.3px}
.dots{left:65px;top:452px;display:flex;gap:4px}
.dots span{width:10px;height:10px;border-radius:50%;background:var(--white)}
.dots span.on{background:#111}

/* services */
.section-title{font-size:22px;font-weight:400;color:var(--ink);letter-spacing:.3px}
.services-title{left:0;width:1040px;top:517px;text-align:center}
.services-intro{left:64px;top:553px;width:912px;text-align:center;font-size:10.5px;line-height:16px;color:var(--text)}
.card{top:604px;width:211px;height:182px;border:1px solid #d6d6d6;background:var(--white)}
.card-photo{position:absolute;left:1px;top:1px;right:1px;height:140px}
.card-label{position:absolute;left:1px;right:1px;bottom:1px;height:39px;background:var(--orange);color:var(--white);font-size:15.5px;font-weight:500;text-align:center;line-height:39px;letter-spacing:.4px}
.card-shadow{top:786px;width:195px;height:8px;background:radial-gradient(ellipse at 50% 0%,rgba(0,0,0,.35),rgba(0,0,0,0) 70%)}

.divider{left:64px;top:829px;width:912px;height:1px;background:var(--line)}

/* showcase */
.showcase-title{left:65px;top:858px}
.showcase-photo{left:64px;top:897px;width:234px;height:138px;border:1px solid #ccc;background:linear-gradient(180deg,#1d3f7a,#3c78c4 55%,#0f1d3a)}
.showcase-copy{left:318px;top:893px;width:334px;font-size:10.5px;line-height:18.4px;color:var(--text)}
.vrule{left:677px;top:862px;width:1px;height:172px;background:var(--line)}
.why-title{left:701px;top:858px}
.why-list{left:701px;top:893px;list-style:none}
.why-list li{display:flex;align-items:center;height:24.8px;font-size:10.5px;color:var(--orange);gap:12px}
.why-list svg{width:10px;height:10px;flex:none}

/* footer */
.footer{left:0;top:1061px;width:1040px;height:139px;background:linear-gradient(180deg,#d8d8d8,#e6e6e6 40%,#e4e4e4)}
.footer-nav{left:66px;top:1086px;font-size:9.6px;color:var(--ink);letter-spacing:.2px;word-spacing:1px}
.footer-nav .sep{margin:0 7px}
.copyright{left:66px;top:1141px;font-size:9.6px;line-height:16px;color:var(--muted)}
.f-head{top:1086px;font-size:11px;color:var(--orange);letter-spacing:.2px}
.f-contact{left:532px;top:1108px;font-size:10.5px;color:var(--ink)}
.f-contact div{display:flex;align-items:center;gap:6px;height:19px}
.f-contact .phone{font-size:12px}
.f-contact svg{width:10px;height:10px}
.f-addr{top:1108px;font-size:9.6px;line-height:16px;color:var(--muted)}
.f-addr .map{display:block;margin-top:4px;color:var(--ink);letter-spacing:.2px}
</style>
</head>
<body>

<header class="abs header">
  <div class="abs brand"><span class="brand-dot"></span>vantora</div>
  <nav class="abs nav">
    <a class="active" href="#">HOME</a>
    <a href="#">SERVICES</a>
    <a href="#">PORTFOLIO</a>
    <a href="#">NEWS</a>
    <a href="#">ABOUT VANTORA</a>
    <a href="#">CONTACT US</a>
  </nav>
</header>

<section class="abs hero" role="img" aria-label="Photo of an engineer in glasses adjusting a precision instrument in a lab"></section>
<h1 class="abs hero-title">Technological Solutions<br>From Idea to Product</h1>
<p class="abs hero-copy">Aliquam molestie, mi et imperdiet euismod, dui purus auctor tellus, et interdum lacus lectus et ante. Sed accumsan sollicitudin sapien, sit amet adipiscing turpis gravida ac. In congue, neque ac lobortis volutpat, libero mauris varius mi, vitae suscipit ipsum ligula vitae risus.</p>
<div class="abs btn">READ MORE</div>
<div class="abs dots"><span class="on"></span><span></span><span></span><span></span></div>

<h2 class="abs section-title services-title">OUR SERVICES</h2>
<p class="abs services-intro">Aliquam molestie, mi et imperdiet euismod, dui purus auctor tellus, et interdum lacus lectus et ante. Sed accumsan sollicitudin sapien, sit amet adipiscing turpis gravida ac. In congue, neque ac lobortis volutpat, libero mauris varius mi, vitae suscipit ipsum ligula vitae risus.</p>

<div class="abs card" style="left:64px">
  <div class="card-photo" role="img" aria-label="Technical drawing with calculator, calipers and drafting tools" style="background:linear-gradient(135deg,#c9d2e0,#eef1f6 55%,#9aa3b3)"></div>
  <div class="card-label">ENGINEERING</div>
</div>
<div class="abs card" style="left:298px">
  <div class="card-photo" role="img" aria-label="Pile of white plastic prototype gears" style="background:linear-gradient(135deg,#d9d9d4,#f1f0ec 50%,#8c8f95)"></div>
  <div class="card-label">PROTOTYPING</div>
</div>
<div class="abs card" style="left:532px">
  <div class="card-photo" role="img" aria-label="Workers in lab coats assembling circuit boards on a line" style="background:linear-gradient(135deg,#8d8f93,#d9d6d0 55%,#5c5a57)"></div>
  <div class="card-label">ASSEMBLING</div>
</div>
<div class="abs card" style="left:766px">
  <div class="card-photo" role="img" aria-label="Technician servicing the inside of a desktop computer" style="background:linear-gradient(135deg,#e4e6ea,#aab4c4 50%,#3c3f46)"></div>
  <div class="card-label">SERVICING</div>
</div>
<div class="abs card-shadow" style="left:72px"></div>
<div class="abs card-shadow" style="left:306px"></div>
<div class="abs card-shadow" style="left:540px"></div>
<div class="abs card-shadow" style="left:774px"></div>

<div class="abs divider"></div>

<h2 class="abs section-title showcase-title">SHOWCASE CLIENT X</h2>
<div class="abs showcase-photo" role="img" aria-label="Silhouettes of two business people shaking hands against a bright window"></div>
<p class="abs showcase-copy">Aliquam molestie, mi et imperdiet euismod, dui purus auctor tellus, et interdum lacus lectus et ante. Sed accumsan sollicitudin sapien, sit amet adipiscing turpis gravida ac. In congue, neque ac lobortis volutpat, libero mauris varius mi, vitae suscipit ipsum ligula vitae risus. Duis aliquam nibh a dui iaculis viverra id a velit. Vivamus egestas risus in magna varius commodo. Sed semper viverra egestas. Etiam pretium porttitor lectus, vel ornare neque porta volutpat. Aenean a nibh eget turpis vehicula tempus ac sed massa.</p>

<div class="abs vrule"></div>

<h2 class="abs section-title why-title">WHY CHOOSE US</h2>
<ul class="abs why-list">
  <li><svg viewBox="0 0 10 10"><path d="M1 5.5 L4 8.5 L9 1.5" fill="none" stroke="#e35c10" stroke-width="2"/></svg>Aliquam molestie, mi et imperdiet euismod</li>
  <li><svg viewBox="0 0 10 10"><path d="M1 5.5 L4 8.5 L9 1.5" fill="none" stroke="#e35c10" stroke-width="2"/></svg>Sed accumsan sollicitudin sapien</li>
  <li><svg viewBox="0 0 10 10"><path d="M1 5.5 L4 8.5 L9 1.5" fill="none" stroke="#e35c10" stroke-width="2"/></svg>In congue, neque ac lobortis</li>
  <li><svg viewBox="0 0 10 10"><path d="M1 5.5 L4 8.5 L9 1.5" fill="none" stroke="#e35c10" stroke-width="2"/></svg>Duis aliquam nibh a dui iaculis viverra id a velit</li>
  <li><svg viewBox="0 0 10 10"><path d="M1 5.5 L4 8.5 L9 1.5" fill="none" stroke="#e35c10" stroke-width="2"/></svg>Vivamus egestas risus in magna</li>
  <li><svg viewBox="0 0 10 10"><path d="M1 5.5 L4 8.5 L9 1.5" fill="none" stroke="#e35c10" stroke-width="2"/></svg>Pellentesque habitant</li>
</ul>

<footer class="abs footer"></footer>
<div class="abs footer-nav">HOME<span class="sep">/</span>SERVICES<span class="sep">/</span>PORTFOLIO<span class="sep">/</span>NEWS<span class="sep">/</span>ABOUT VANTORA<span class="sep">/</span>CONTACT US</div>
<div class="abs copyright">Copyright © 2015 VANTORA HOLDINGS INTERNATIONAL, LTD<br>All Rights Reserved</div>

<div class="abs f-head" style="left:532px">CONTACT INFO</div>
<div class="abs f-contact">
  <div><svg viewBox="0 0 10 10"><rect x="0.5" y="2" width="9" height="6.5" fill="#333"/><path d="M0.5 2 L5 5.8 L9.5 2" fill="none" stroke="#e0e0e0" stroke-width="1"/></svg>info@vantora-eng.com</div>
  <div class="phone"><svg viewBox="0 0 10 10"><rect x="0.5" y="0.5" width="9" height="9" rx="1.5" fill="#333"/><path d="M3 2.5 L4.2 2.5 L4.7 4 L4 4.6 Q4.8 6 6 6.3 L6.5 5.6 L8 6 L8 7.3 Q5 7.5 3 4.2 Z" fill="#e0e0e0"/></svg>+86-21-5550-0142</div>
</div>

<div class="abs f-head" style="left:690px">OUR SALES DEPARTMENT</div>
<div class="abs f-addr" style="left:690px">1200 Fenwick<br>Road,Glasgow, G12 7QX<span class="map">VIEW MAP</span></div>

<div class="abs f-head" style="left:863px">R&amp;D &amp; PRODUCTION</div>
<div class="abs f-addr" style="left:863px">1200 Fenwick<br>Road,Glasgow, G12 7QX<span class="map">VIEW MAP</span></div>

</body>
</html>
```